Interior design service, along with home organization, packing, and staging, home and business. As well as staging in conjunction with real estate sales.
Updates

Love many of your designs and will be choosing today. To inform you of the exact details needed, the name of the company is "Touches by Marla T" , my phone number and e-,ail need to be included. i also need either description or some sort of bullet points that give an idea of the following:

- Interior design for home and business
- Home organization and packing
- Staging for personal and professional space
- Real estate stagingĀ 

Thank you

Target Market(s)

wide audience, but most importantly people looking for a quality service

Industry/Entity Type

Real Estate

Contact Information for Business Card

Touches By Marla T
Marla Tovendi
(555)614-2937
mtbrook@mailnest.example

Requirements
Must have
• I'm 29 so i want my card to reflect something professional but still fresh. I don't have any specific photos or quotes that Ive included, however I like the card to reflect a personal touch, which is what I'm seeking from this service in the design of my card. Thanks!

```html
<!DOCTYPE html>
<html lang="en">
<head>
<meta charset="utf-8">
<title>Touches by Marla T – Business Card</title>
<link href="https://fonts.googleapis.com/css2?family=Inter:wght@200;300&display=swap" rel="stylesheet">
<style>
  :root {
    --paper: #ffffff;
    --ink: #1a1a1a;
    --accent: #5a2cff;
    --accent-soft: #8a5cff;
  }
  html, body {
    margin: 0;
    padding: 0;
    overflow: hidden;
    background: var(--paper);
  }
  .card {
    position: relative;
    width: 1200px;
    height: 702px;
    background: var(--paper);
    font-family: "Inter", "Helvetica Neue", Arial, sans-serif;
    font-weight: 200;
    color: var(--ink);
    overflow: hidden;
  }
  .company-name {
    position: absolute;
    left: 60px;
    top: 96px;
    margin: 0;
    font-size: 30px;
    line-height: 1;
    letter-spacing: 0.3em;
    font-weight: 200;
    color: var(--accent);
    white-space: nowrap;
  }
  .contact-line {
    position: absolute;
    left: 60px;
    margin: 0;
    font-size: 52px;
    line-height: 1;
    letter-spacing: 0.3em;
    white-space: nowrap;
    font-weight: 200;
  }
  .owner-name { top: 343px; color: var(--accent); }
  .phone { top: 424px; }
  .email { top: 500px; letter-spacing: 0.27em; }
  .services {
    position: absolute;
    top: 632px;
    left: 0;
    width: 1200px;
    height: 28px;
    margin: 0;
    padding: 0;
    list-style: none;
  }
  .service {
    position: absolute;
    top: 0;
    font-size: 20px;
    font-weight: 300;
    line-height: 1;
    letter-spacing: 0.24em;
    white-space: nowrap;
  }
  .service--design { left: 59px; }
  .service--organize { left: 428px; }
  .service--staging { left: 853px; }
  .separator-mark {
    position: absolute;
    top: 0;
    width: 22px;
    height: 22px;
    background: linear-gradient(135deg, var(--accent-soft) 0%, var(--accent) 100%);
  }
  .separator-mark--first { left: 337px; }
  .separator-mark--second { left: 762px; }
</style>
</head>
<body>
  <div class="card">
    <p class="company-name">Touches by Marla T</p>

    <p class="contact-line owner-name">Marla Tovendi</p>
    <p class="contact-line phone">(555)614-2937</p>
    <p class="contact-line email">mtbrook@mailnest.example</p>

    <ul class="services">
      <li class="service service--design">Interior Design</li>
      <li class="separator-mark separator-mark--first" role="img" aria-label="Small violet brush-stroke ornament separating services"></li>
      <li class="service service--organize">Home Organization</li>
      <li class="separator-mark separator-mark--second" role="img" aria-label="Small violet brush-stroke ornament separating services"></li>
      <li class="service service--staging">Packing and Staging</li>
    </ul>
  </div>
</body>
</html>
```